TEFL Internship Page Redesign

Hi guys! I have put together a design brief in this document - https://files.plimworth.net/sheet/d/7kq2Zx_P-4bwTrNmL9x83vHcYsW0qE5dJfAaB21tuu/view. I have made sure to give access.

Please read carefully and elevate the current design on the link provided. I have tried to give some much specifics as possible. Where I haven't please use your judgement to come with something. For all text please use "poppins".

```html
<!DOCTYPE html>
<html lang="en">
<head>
<meta charset="utf-8">
<title>TEFL Internships – Linguaro Academy</title>
<link href="https://fonts.googleapis.com/css2?family=Poppins:wght@300;400;500;600;700&family=Dancing+Script:wght@600;700&display=swap" rel="stylesheet">
<style>
:root{
  --teal:#1cc3d3;
  --teal-dark:#12a9b8;
  --ink:#1d1d1f;
  --text:#555b61;
  --muted:#8a9096;
  --grey-bg:#f3f4f5;
  --navy:#213e5a;
  --footer:#15909d;
  --footer-deep:#0d6370;
  --orange:#f08a4b;
  --white:#ffffff;
  --line:#e3e6e8;
}
*{box-sizing:border-box;margin:0;padding:0}
html,body{width:1200px;height:4914px;overflow:hidden}
body{font-family:"Poppins",sans-serif;color:var(--text);background:var(--white);position:relative}
.section{position:absolute;left:0;width:1200px}
ul{list-style:none}

/* top bar + hero */
.topbar{top:0;height:38px;background:rgba(20,20,20,.92);z-index:3;display:flex;align-items:center;justify-content:space-between;padding:0 14px;font-size:10px;color:#fff}
.topbar .hl{color:var(--teal)}
.topbar .right{display:flex;gap:14px;align-items:center}
.topbar .flag{display:inline-block;width:16px;height:10px;background:var(--orange);vertical-align:middle;margin-right:4px}
.hero{top:0;height:535px;background:linear-gradient(180deg,#6d6a73 0%,#8f6b68 45%,#5b4b50 100%)}
.hero .photo{position:absolute;inset:0}
.hero .shade{position:absolute;inset:0;background:linear-gradient(180deg,rgba(0,0,0,.25),rgba(0,0,0,.05) 40%,rgba(0,0,0,.2))}
.nav{position:absolute;top:48px;left:14px;right:14px;display:flex;justify-content:space-between;align-items:flex-start}
.brand{display:flex;align-items:center;gap:8px;color:#fff;font-weight:700;font-size:26px;letter-spacing:.5px}
.brand .dot{width:14px;height:14px;background:var(--teal)}
.menu{display:flex;gap:16px;font-size:10px;color:#fff;align-items:center;margin-top:34px}
.search{position:absolute;top:48px;right:72px;width:170px;height:20px;border:1px solid rgba(255,255,255,.6);font-size:9px;color:#ddd;padding:3px 6px}
.enrol{position:absolute;top:48px;right:14px;background:var(--teal);color:#fff;font-size:9px;padding:4px 10px}
.hero h1{position:absolute;top:216px;width:100%;text-align:center;color:#fff;font-size:36px;font-weight:700}
.hero .tagline{position:absolute;top:258px;width:100%;text-align:center;color:#fff;font-family:"Dancing Script",cursive;font-size:32px;font-weight:600}
.band{top:535px;height:47px;background:var(--navy);color:#dfe6ec;font-size:11px;display:flex;align-items:center;justify-content:center;gap:6px}
.band b{color:var(--teal)}

/* internship cards */
.programs{top:582px;height:1183px;background:var(--grey-bg)}
.cards{position:absolute;top:68px;left:143px;display:flex;gap:20px}
.card{width:214px;height:1048px;background:var(--white);display:flex;flex-direction:column;position:relative}
.card.active{outline:2px solid var(--teal)}
.card .media{height:212px;position:relative;overflow:hidden}
.card .media .fill{position:absolute;inset:0}
.card .media .place{position:absolute;top:118px;width:100%;text-align:center;color:#fff;font-family:"Dancing Script",cursive;font-size:36px;font-weight:700}
.card .media .sub{position:absolute;top:172px;width:100%;text-align:center;color:#fff;font-size:11px}
.card .media svg{position:absolute;bottom:0;left:0}
.card .body{padding:14px 16px 0;flex:1}
.row{border-bottom:1px solid var(--line);padding:10px 0 16px}
.row:last-child{border:0}
.label{display:flex;align-items:center;gap:10px;color:var(--teal);font-weight:600;font-size:12px;margin-bottom:12px}
.val{font-size:11px;color:var(--ink);line-height:1.9}
.benefits li{font-size:9.5px;line-height:1.75;color:var(--text);padding-left:12px;position:relative;margin-bottom:9px}
.benefits li::before{content:"";position:absolute;left:0;top:6px;width:4px;height:4px;border-radius:50%;background:var(--teal)}
.card .actions{display:flex;height:28px}
.btn{display:flex;align-items:center;justify-content:center;font-size:10px;font-weight:600;color:#fff;text-transform:uppercase}
.actions .btn{flex:1}
.btn.teal{background:var(--teal)}
.btn.dark{background:var(--ink)}
.arrow{position:absolute;top:160px;width:22px;height:22px;border-radius:50%;display:flex;align-items:center;justify-content:center;z-index:2;box-shadow:0 1px 4px rgba(0,0,0,.2)}
.arrow.prev{left:131px;background:#fff}
.arrow.next{left:1045px;background:var(--teal)}

/* intro + faq */
.intro{top:1765px;height:582px}
.intro h2,.faq h2{font-size:25px;font-weight:600;color:#3b3f44}
.intro .copy{position:absolute;left:143px;top:72px;width:415px}
.lead{margin:30px 0 26px;border-left:3px solid var(--teal);padding-left:18px;color:var(--teal);font-size:14px;line-height:1.8}
.copy p{font-size:11px;line-height:2.1;margin-bottom:24px}
.faq{position:absolute;left:647px;top:70px;width:410px}
.faq h2{margin-bottom:28px}
.q{border:1px solid var(--line);height:42px;display:flex;align-items:center;justify-content:space-between;padding:0 16px;font-size:10.5px;color:#555;margin-bottom:15px}
.q.open{background:var(--teal);color:#fff;border-color:var(--teal);margin-bottom:0;font-weight:600}
.answer{border:1px solid var(--teal);border-top:0;padding:18px 22px;font-size:10.5px;line-height:2.1;margin-bottom:15px}

/* how it works */
.how{top:2347px;height:477px;background:var(--teal);color:#fff}
.how h2{position:absolute;top:52px;width:100%;text-align:center;font-size:25px;font-weight:600}
.steps{position:absolute;top:148px;left:0;width:100%}
.step{position:absolute;width:200px;text-align:center;transform:translateX(-50%)}
.step .ring{width:104px;height:104px;border-radius:50%;background:#fff;margin:0 auto;display:flex;align-items:center;justify-content:center}
.step .num{width:20px;height:20px;border-radius:50%;background:#fff;color:var(--teal);font-size:10px;font-weight:600;margin:26px auto 0;display:flex;align-items:center;justify-content:center}
.step .num.alt{background:var(--orange);color:#fff}
.step h3{font-size:15px;font-weight:600;margin-top:14px}
.step p{font-size:11px;line-height:1.95;margin-top:10px;color:#e9fbfd}
.dots{position:absolute;top:137px;left:250px;width:698px;border-top:2px dotted rgba(255,255,255,.8)}

/* help */
.help{top:2824px;height:525px}
.help h2{position:absolute;top:52px;width:100%;text-align:center;font-size:25px;font-weight:600;color:#3b3f44}
.box{position:absolute;top:118px;width:372px;height:330px;background:var(--grey-bg);text-align:center;padding-top:30px}
.box .icon{width:90px;height:90px;border-radius:50%;margin:0 auto;display:flex;align-items:center;justify-content:center}
.box h3{font-size:16px;font-weight:600;color:#444;margin-top:34px}
.box p{font-size:10.5px;line-height:2;margin:18px auto 0;width:300px}
.box .btn{width:194px;height:34px;margin:30px auto 0}
.box .bar{position:absolute;bottom:0;left:0;right:0;height:5px}

/* articles */
.articles{top:3349px;height:934px}
.articles h2{position:absolute;top:55px;width:100%;text-align:center;font-size:25px;font-weight:600;color:#3b3f44}
.post{position:absolute;width:294px;height:318px;background:var(--white);border:1px solid var(--line);padding:13px 13px 0}
.post.active{border:2px solid var(--teal)}
.post .thumb{height:200px}
.meta{display:flex;justify-content:space-between;font-size:9px;color:var(--teal);margin-top:12px}
.meta span{display:flex;align-items:center;gap:5px}
.post h4{font-size:11px;font-weight:600;color:#333;line-height:1.9;margin-top:9px}
.viewall{position:absolute;top:816px;left:494px;width:212px;height:46px;font-size:11px}

/* footer */
.footer{top:4283px;height:631px;background:var(--footer);color:#fff}
.footer .edge{position:absolute;top:-1px;left:0}
.footer .brand{position:absolute;top:80px;width:100%;justify-content:center;font-size:30px}
.cols{position:absolute;top:170px;left:280px;display:flex;gap:36px}
.col{width:98px;text-align:center}
.col h5{font-size:11px;font-weight:600;line-height:1.3;margin-bottom:10px}
.col li{font-size:8.5px;line-height:1.35;margin-bottom:9px;color:#e5f7f9}
.base{position:absolute;top:439px;left:0;width:100%;height:192px;background:var(--footer-deep)}
.base .call{position:absolute;top:62px;width:100%;text-align:center;font-size:10px;font-weight:600}
.base .legal{position:absolute;top:100px;width:100%;text-align:center;font-size:8px;color:#d7eef1;line-height:2.2}
.pay{position:absolute;top:86px;left:22px;display:flex;gap:20px}
.pay i{display:block;width:34px;height:20px;background:#fff;border-radius:3px}
.social{position:absolute;top:86px;right:22px;display:flex;gap:12px}
.social i{display:block;width:22px;height:22px;border-radius:50%;background:#fff}
.copyright{position:absolute;bottom:0;width:100%;height:30px;background:#fff;color:#666;font-size:8px;display:flex;align-items:center;justify-content:center}
</style>
</head>
<body>

<header class="section hero">
  <div class="photo" role="img" aria-label="Photo of a teacher leading a line of young pupils in school uniforms outdoors"></div>
  <div class="shade"></div>
  <div class="nav">
    <div class="brand"><span class="dot"></span>Linguaro</div>
    <nav class="menu"><span>Why Linguaro ▾</span><span>TEFL Courses ▾</span><span>Teach English Online ▾</span><span>Teaching Opportunities ▾</span><span>Jobs</span><span>Blog</span><span>Support ▾</span></nav>
  </div>
  <div class="search">Search</div>
  <div class="enrol">Enrol Me ›</div>
  <h1>TEFL Internships</h1>
  <div class="tagline">Teach Enrich Empower</div>
</header>

<div class="section topbar">
  <div>Call us for help <span class="hl">+1 555 013 4210</span> &nbsp;&nbsp; Request a callback</div>
  <div class="right"><span class="hl">How TEFL Works</span><span>Log In</span><span class="hl">Visit our international sites</span><span><i class="flag"></i>INDIA</span></div>
</div>

<div class="section band">Join a global community of over 200,000 TEFL teachers working throughout the world! <b>Enrol me!</b></div>

<section class="section programs">
  <div class="arrow prev"><svg width="8" height="8" viewBox="0 0 8 8"><path d="M5.5 1 2.5 4l3 3" fill="none" stroke="#555" stroke-width="1.4"/></svg></div>
  <div class="arrow next"><svg width="8" height="8" viewBox="0 0 8 8"><path d="M2.5 1l3 3-3 3" fill="none" stroke="#fff" stroke-width="1.4"/></svg></div>
  <div class="cards">

    <article class="card">
      <div class="media">
        <div class="fill" role="img" aria-label="Photo of schoolchildren in Argentina" style="background:linear-gradient(160deg,#7b6f66,#3e3a38)"></div>
        <div class="place">Argentina</div><div class="sub">TEFL Internship Argentina</div>
        <svg width="214" height="10" viewBox="0 0 214 10"><path d="M0 10V4l6 6 6-6 6 6 6-6 6 6 6-6 6 6 6-6 6 6 6-6 6 6 6-6 6 6 6-6 6 6 6-6 6 6 6-6 6 6 6-6 6 6 6-6 6 6 6-6 6 6 6-6 6 6 6-6 6 6 6-6 6 6 6-6 6 6 6-6 6 6 6-6 6 6 6-6 6 6 6-6 6 6 6-6 6 6 6-6 4 4z" fill="#fff"/></svg>
      </div>
      <div class="body">
        <div class="row"><div class="label"><svg width="18" height="14" viewBox="0 0 18 14"><rect x="1" y="2" width="16" height="10" rx="1" fill="none" stroke="#1cc3d3" stroke-width="1.5"/><path d="M1 5h16" stroke="#1cc3d3" stroke-width="1.5"/></svg>Price:</div><div class="val">£699GBP, $910USD, R13,215ZAR, $1,150CAD, $765NZD, $1,225AUD, €840EUR</div></div>
        <div class="row"><div class="label"><svg width="16" height="16" viewBox="0 0 16 16"><rect x="1" y="3" width="14" height="12" rx="1" fill="none" stroke="#1cc3d3" stroke-width="1.5"/><path d="M1 7h14M5 1v4M11 1v4" stroke="#1cc3d3" stroke-width="1.5"/></svg>Starts :</div><div class="val">February &amp; July</div></div>
        <div class="row"><div class="label"><svg width="18" height="16" viewBox="0 0 18 16"><rect x="1" y="1" width="14" height="11" fill="none" stroke="#1cc3d3" stroke-width="1.5"/><rect x="5" y="6" width="12" height="9" fill="#1cc3d3"/></svg>Living allowance :</div><div class="val">$600 - $1,200 per month</div></div>
        <div class="row"><div class="label"><svg width="16" height="16" viewBox="0 0 16 16"><path d="M8 1l2 5h5l-4 3 1.5 5L8 11l-4.5 3L5 9 1 6h5z" fill="#1cc3d3"/></svg>Benefits:</div>
          <ul class="benefits"><li>A monthly stipend of $600 - $1,200</li><li>Airport transfer upon arrival in Buenos Aires</li><li>Free transfer to host town/city</li><li>Home-stay accommodation with an Argentine host family</li><li>4 hours of one-to-one Spanish lessons weekly</li><li>Transport and full-board accom-modation during immersion Camps</li><li>Certification upon completion of the programme</li><li>Monthly follow-up contact through the local office</li><li>24/7 emergency support</li></ul></div>
        <div class="row"><div class="label"><svg width="16" height="16" viewBox="0 0 16 16"><rect x="1" y="3" width="14" height="12" rx="1" fill="none" stroke="#1cc3d3" stroke-width="1.5"/><path d="M1 7h14M5 1v4M11 1v4" stroke="#1cc3d3" stroke-width="1.5"/></svg>Duration:</div><div class="val">3 or 12 Months</div></div>
      </div>
      <div class="actions"><a class="btn teal">More Info</a><a class="btn dark">Apply Now</a></div>
    </article>

    <article class="card active">
      <div class="media">
        <div class="fill" role="img" aria-label="Photo of red paper lanterns at night in Sichuan" style="background:linear-gradient(160deg,#3b2a2a,#c9603a 60%,#2a1c1c)"></div>
        <div class="place">China</div><div class="sub">TEFL Internship Sichuan</div>
        <svg width="214" height="10" viewBox="0 0 214 10"><path d="M0 10V4l6 6 6-6 6 6 6-6 6 6 6-6 6 6 6-6 6 6 6-6 6 6 6-6 6 6 6-6 6 6 6-6 6 6 6-6 6 6 6-6 6 6 6-6 6 6 6-6 6 6 6-6 6 6 6-6 6 6 6-6 6 6 6-6 6 6 6-6 6 6 6-6 6 6 6-6 6 6 6-6 6 6 6-6 6 6 6-6 4 4z" fill="#fff"/></svg>
      </div>
      <div class="body">
        <div class="row"><div class="label"><svg width="18" height="14" viewBox="0 0 18 14"><rect x="1" y="2" width="16" height="10" rx="1" fill="none" stroke="#1cc3d3" stroke-width="1.5"/><path d="M1 5h16" stroke="#1cc3d3" stroke-width="1.5"/></svg>Price:</div><div class="val">No fee!</div></div>
        <div class="row"><div class="label"><svg width="16" height="16" viewBox="0 0 16 16"><rect x="1" y="3" width="14" height="12" rx="1" fill="none" stroke="#1cc3d3" stroke-width="1.5"/><path d="M1 7h14M5 1v4M11 1v4" stroke="#1cc3d3" stroke-width="1.5"/></svg>Starts :</div><div class="val">February &amp; August</div></div>
        <div class="row"><div class="label"><svg width="18" height="16" viewBox="0 0 18 16"><rect x="1" y="1" width="14" height="11" fill="none" stroke="#1cc3d3" stroke-width="1.5"/><rect x="5" y="6" width="12" height="9" fill="#1cc3d3"/></svg>Living allowance :</div><div class="val">RMB 6,000 monthly salary</div></div>
        <div class="row"><div class="label"><svg width="16" height="16" viewBox="0 0 16 16"><path d="M8 1l2 5h5l-4 3 1.5 5L8 11l-4.5 3L5 9 1 6h5z" fill="#1cc3d3"/></svg>Benefits:</div>
          <ul class="benefits"><li>A monthly stipend of $600 - $1,200</li><li>Airport transfer upon arrival in Buenos Aires</li><li>Free transfer to host town/city</li><li>Home-stay accommodation with an Argentine host family</li><li>4 hours of one-to-one Spanish lessons weekly</li><li>Transport and full-board accom-modation during immersion Camps</li><li>Certification upon completion of the programme</li><li>Monthly follow-up contact through the local office</li><li>24/7 emergency support</li><li>Sponsored by local government in Sichuan</li></ul></div>
        <div class="row"><div class="label"><svg width="16" height="16" viewBox="0 0 16 16"><rect x="1" y="3" width="14" height="12" rx="1" fill="none" stroke="#1cc3d3" stroke-width="1.5"/><path d="M1 7h14M5 1v4M11 1v4" stroke="#1cc3d3" stroke-width="1.5"/></svg>Duration:</div><div class="val">3 or 12 Months</div></div>
      </div>
      <div class="actions"><a class="btn teal">More Info</a><a class="btn dark">Apply Now</a></div>
    </article>

    <article class="card">
      <div class="media">
        <div class="fill" role="img" aria-label="Photo of the Shanghai skyline at dusk" style="background:linear-gradient(180deg,#8da3c9,#b7a4c8 55%,#4b4a6a)"></div>
        <div class="place">China</div><div class="sub">TEFL Internship Shanghai</div>
        <svg width="214" height="10" viewBox="0 0 214 10"><path d="M0 10V4l6 6 6-6 6 6 6-6 6 6 6-6 6 6 6-6 6 6 6-6 6 6 6-6 6 6 6-6 6 6 6-6 6 6 6-6 6 6 6-6 6 6 6-6 6 6 6-6 6 6 6-6 6 6 6-6 6 6 6-6 6 6 6-6 6 6 6-6 6 6 6-6 6 6 6-6 6 6 6-6 6 6 6-6 6 6 6-6 4 4z" fill="#fff"/></svg>
      </div>
      <div class="body">
        <div class="row"><div class="label"><svg width="18" height="14" viewBox="0 0 18 14"><rect x="1" y="2" width="16" height="10" rx="1" fill="none" stroke="#1cc3d3" stroke-width="1.5"/><path d="M1 5h16" stroke="#1cc3d3" stroke-width="1.5"/></svg>Price:</div><div class="val">No fee!</div></div>
        <div class="row"><div class="label"><svg width="16" height="16" viewBox="0 0 16 16"><rect x="1" y="3" width="14" height="12" rx="1" fill="none" stroke="#1cc3d3" stroke-width="1.5"/><path d="M1 7h14M5 1v4M11 1v4" stroke="#1cc3d3" stroke-width="1.5"/></svg>Starts :</div><div class="val">Year-round</div></div>
        <div class="row"><div class="label"><svg width="18" height="16" viewBox="0 0 18 16"><rect x="1" y="1" width="14" height="11" fill="none" stroke="#1cc3d3" stroke-width="1.5"/><rect x="5" y="6" width="12" height="9" fill="#1cc3d3"/></svg>Living allowance :</div><div class="val">RMB 4,000 per month</div></div>
        <div class="row"><div class="label"><svg width="16" height="16" viewBox="0 0 16 16"><path d="M8 1l2 5h5l-4 3 1.5 5L8 11l-4.5 3L5 9 1 6h5z" fill="#1cc3d3"/></svg>Benefits:</div>
          <ul class="benefits"><li>A monthly stipend of $600 - $1,200</li><li>Airport transfer upon arrival in Buenos Aires</li><li>Free transfer to host town/city</li><li>Home-stay accommodation with an Argentine host family</li><li>4 hours of one-to-one Spanish lessons weekly</li><li>Transport and full-board accom-modation during immersion Camps</li><li>Certification upon completion of the programme</li><li>Monthly follow-up contact through the local office</li><li>24/7 emergency support</li><li>Sponsored by local government in Sichuan</li></ul></div>
        <div class="row"><div class="label"><svg width="16" height="16" viewBox="0 0 16 16"><rect x="1" y="3" width="14" height="12" rx="1" fill="none" stroke="#1cc3d3" stroke-width="1.5"/><path d="M1 7h14M5 1v4M11 1v4" stroke="#1cc3d3" stroke-width="1.5"/></svg>Duration:</div><div class="val">4.5 Months</div></div>
      </div>
      <div class="actions"><a class="btn teal">More Info</a><a class="btn dark">Apply Now</a></div>
    </article>

    <article class="card">
      <div class="media">
        <div class="fill" role="img" aria-label="Photo of a neon-lit street in South Korea" style="background:linear-gradient(160deg,#2b6f9a,#173a5c 55%,#8a2d3a)"></div>
        <div class="place">Korea, South</div><div class="sub">TEFL Internship South Korea</div>
        <svg width="214" height="10" viewBox="0 0 214 10"><path d="M0 10V4l6 6 6-6 6 6 6-6 6 6 6-6 6 6 6-6 6 6 6-6 6 6 6-6 6 6 6-6 6 6 6-6 6 6 6-6 6 6 6-6 6 6 6-6 6 6 6-6 6 6 6-6 6 6 6-6 6 6 6-6 6 6 6-6 6 6 6-6 6 6 6-6 6 6 6-6 6 6 6-6 6 6 6-6 6 6 6-6 6 6 6-6 4 4z" fill="#fff"/></svg>
      </div>
      <div class="body">
        <div class="row"><div class="label"><svg width="18" height="14" viewBox="0 0 18 14"><rect x="1" y="2" width="16" height="10" rx="1" fill="none" stroke="#1cc3d3" stroke-width="1.5"/><path d="M1 5h16" stroke="#1cc3d3" stroke-width="1.5"/></svg>Price:</div><div class="val">No fee!</div></div>
        <div class="row"><div class="label"><svg width="16" height="16" viewBox="0 0 16 16"><rect x="1" y="3" width="14" height="12" rx="1" fill="none" stroke="#1cc3d3" stroke-width="1.5"/><path d="M1 7h14M5 1v4M11 1v4" stroke="#1cc3d3" stroke-width="1.5"/></svg>Starts :</div><div class="val">Year-round</div></div>
        <div class="row"><div class="label"><svg width="18" height="16" viewBox="0 0 18 16"><rect x="1" y="1" width="14" height="11" fill="none" stroke="#1cc3d3" stroke-width="1.5"/><rect x="5" y="6" width="12" height="9" fill="#1cc3d3"/></svg>Living allowance :</div><div class="val">RMB 4,000 per month</div></div>
        <div class="row"><div class="label"><svg width="16" height="16" viewBox="0 0 16 16"><path d="M8 1l2 5h5l-4 3 1.5 5L8 11l-4.5 3L5 9 1 6h5z" fill="#1cc3d3"/></svg>Benefits:</div>
          <ul class="benefits"><li>A monthly stipend of $600 - $1,200</li><li>Airport transfer upon arrival in Buenos Aires</li><li>Free transfer to host town/city</li><li>Home-stay accommodation with an Argentine host family</li><li>4 hours of one-to-one Spanish lessons weekly</li><li>Transport and full-board accom-modation during immersion Camps</li><li>Certification upon completion of the programme</li><li>Monthly follow-up contact through the local office</li><li>24/7 emergency support</li><li>Sponsored by local government in Sichuan</li></ul></div>
        <div class="row"><div class="label"><svg width="16" height="16" viewBox="0 0 16 16"><rect x="1" y="3" width="14" height="12" rx="1" fill="none" stroke="#1cc3d3" stroke-width="1.5"/><path d="M1 7h14M5 1v4M11 1v4" stroke="#1cc3d3" stroke-width="1.5"/></svg>Duration:</div><div class="val">4.5 Months</div></div>
      </div>
      <div class="actions"><a class="btn teal">More Info</a><a class="btn dark">Apply Now</a></div>
    </article>

  </div>
</section>

<section class="section intro">
  <div class="copy">
    <h2>TEFL Internships</h2>
    <p class="lead">Our TEFL internships are a great way to start your new career. Get paid a great salary and receive support throughout your contract!</p>
    <p>Our TEFL internships are open to anyone who has enrolled on the Level 3 or Level 5 version of our TEFL course and meets the requirements listed for each opportunity. Our TEFL internships are the fastest way to kick start your TEFL career whilst receiving a higher level of support than standard TEFL jobs.</p>
    <p>Most of our TEFL internships will include 24×7 local support, an orientation week with lots of other foreign teachers, excursions, accommodation, living allowance, help getting a bank account and sim card, and fewer working hours than a standard contracted teacher. Our TEFL internships are the perfect way to bridge the gap between qualifying and starting a more formal teaching role.</p>
  </div>
  <div class="faq">
    <h2>Frequently Asked Questions</h2>
    <div class="q open">Do I need to be a native English speaker study the course? <svg width="10" height="6" viewBox="0 0 10 6"><path d="M1 1l4 4 4-4" fill="none" stroke="#fff" stroke-width="1.4"/></svg></div>
    <div class="answer">Your current or future customer is not interested in your product, they are interested in solving a problem or challenge, usually both organizational and personal.</div>
    <div class="q">What level should my English be? <svg width="10" height="6" viewBox="0 0 10 6"><path d="M1 1l4 4 4-4" fill="none" stroke="#666" stroke-width="1.4"/></svg></div>
    <div class="q">Who can I teach when I have completed the course? <svg width="10" height="6" viewBox="0 0 10 6"><path d="M1 1l4 4 4-4" fill="none" stroke="#666" stroke-width="1.4"/></svg></div>
    <div class="q">How soon can I start applying for TEFL Jobs? <svg width="10" height="6" viewBox="0 0 10 6"><path d="M1 1l4 4 4-4" fill="none" stroke="#666" stroke-width="1.4"/></svg></div>
    <div class="q">What technology will I need to do the online course? <svg width="10" height="6" viewBox="0 0 10 6"><path d="M1 1l4 4 4-4" fill="none" stroke="#666" stroke-width="1.4"/></svg></div>
  </div>
</section>

<section class="section how">
  <h2>How It Works</h2>
  <div class="steps">
    <div class="dots"></div>
    <div class="step" style="left:250px">
      <div class="ring"><svg width="44" height="44" viewBox="0 0 44 44"><rect x="4" y="8" width="36" height="26" rx="2" fill="#1cc3d3"/><rect x="8" y="13" width="12" height="8" fill="#fff"/><path d="M24 14h12M24 19h12M8 26h28" stroke="#fff" stroke-width="2"/><ellipse cx="22" cy="36" rx="12" ry="4" fill="none" stroke="#1d1d1f" stroke-width="2"/></svg></div>
      <div class="num">1</div><h3>Apply</h3><p>Donec pulinar magna id leo pelsque perdied digssim euimod eros vitae</p>
    </div>
    <div class="step" style="left:483px">
      <div class="ring"><svg width="44" height="44" viewBox="0 0 44 44"><circle cx="15" cy="13" r="6" fill="#f08a4b"/><path d="M5 32c0-7 4-11 10-11s10 4 10 11z" fill="#f08a4b"/><rect x="24" y="9" width="16" height="10" rx="2" fill="#1cc3d3"/><circle cx="31" cy="26" r="4" fill="#1d1d1f"/><path d="M24 38c0-5 3-7 7-7s7 2 7 7z" fill="#1d1d1f"/></svg></div>
      <div class="num alt">2</div><h3>Interview</h3><p>Donec pulinar magna id leo pelsque perdied digssim euimod eros vitae</p>
    </div>
    <div class="step" style="left:717px">
      <div class="ring"><svg width="44" height="44" viewBox="0 0 44 44"><rect x="13" y="6" width="22" height="30" rx="2" fill="#1cc3d3"/><rect x="9" y="10" width="22" height="30" rx="2" fill="#17aebf"/><path d="M14 18h12M14 23h12M14 28h12M14 33h8" stroke="#fff" stroke-width="2"/></svg></div>
      <div class="num">3</div><h3>Document</h3><p>Donec pulinar magna id leo pelsque perdied digssim euimod eros vitae</p>
    </div>
    <div class="step" style="left:948px">
      <div class="ring"><svg width="44" height="44" viewBox="0 0 44 44"><rect x="6" y="6" width="30" height="22" rx="1" fill="#f08a4b"/><rect x="9" y="9" width="24" height="16" fill="#fde3d1"/><path d="M12 20l5-5 4 3 6-6" fill="none" stroke="#f08a4b" stroke-width="2"/><circle cx="34" cy="30" r="4" fill="#1cc3d3"/><path d="M27 42c0-5 3-7 7-7s7 2 7 7z" fill="#1cc3d3"/></svg></div>
      <div class="num alt">4</div><h3>Teach!</h3><p>Donec pulinar magna id leo pelsque perdied digssim euimod eros vitae</p>
    </div>
  </div>
</section>

<section class="section help">
  <h2>Need Further Help..?</h2>
  <div class="box" style="left:204px">
    <div class="icon" style="background:var(--teal)"><svg width="46" height="46" viewBox="0 0 46 46"><path d="M34 8c-10 1-17 8-21 18l7 7c10-4 17-11 18-21z" fill="none" stroke="#fff" stroke-width="2.4" stroke-linejoin="round"/><circle cx="28" cy="18" r="3" fill="#fff"/><path d="M13 26l-5 1 3-7 6-1M20 33l-1 5 7-3 1-6M10 36l4-4M14 38l2-2M8 32l2-2" stroke="#fff" stroke-width="2.2" fill="none" stroke-linecap="round"/></svg></div>
    <h3>Get Started</h3>
    <p>Aliquam sodales justo sit amet urna auctor scelerisquinterd um leo antetpus enim esent egetis hendrerit vel nibh vitae ornar sem.</p>
    <a class="btn teal">Request a Callback</a>
    <div class="bar" style="background:var(--teal)"></div>
  </div>
  <div class="box" style="left:623px">
    <div class="icon" style="background:var(--ink)"><svg width="46" height="46" viewBox="0 0 46 46"><path d="M12 6h16l8 8v24H12z" fill="none" stroke="#fff" stroke-width="2.2" stroke-linejoin="round"/><path d="M28 6v8h8" fill="none" stroke="#fff" stroke-width="2.2"/><circle cx="28" cy="32" r="8" fill="#1d1d1f" stroke="#fff" stroke-width="2.2"/><path d="M28 27v9M24.5 33l3.5 3.5 3.5-3.5" fill="none" stroke="#fff" stroke-width="2"/></svg></div>
    <h3>Download Guide</h3>
    <p>Aliquam sodales justo sit amet urna auctor scelerisquinterd um leo antetpus enim esent egetis hendrerit vel nibh vitae ornar sem.</p>
    <a class="btn dark">Download “TEFL Guide”</a>
    <div class="bar" style="background:var(--ink)"></div>
  </div>
</section>

<section class="section articles">
  <h2>Internship Articles</h2>
  <article class="post" style="left:143px;top:133px">
    <div class="thumb" role="img" aria-label="Photo of a woman working on a laptop at home" style="background:linear-gradient(150deg,#e9e2d8,#b49a80)"></div>
    <div class="meta"><span>▣ 23rd March 2023</span><span>● Maya Lorne</span></div>
    <h4>From Zero to Hero: Cool (Free) Resources to Make Your Online Lessons Amazing</h4>
  </article>
  <article class="post active" style="left:455px;top:133px">
    <div class="thumb" role="img" aria-label="Photo of a smiling teacher with a group of pupils" style="background:linear-gradient(150deg,#6d7a86,#c9b49c)"></div>
    <div class="meta"><span>▣ 23rd March 2023</span><span>● Maya Lorne</span></div>
    <h4>TEFL 2023: Is It Still Worth Doing?</h4>
  </article>
  <article class="post" style="left:763px;top:133px">
    <div class="thumb" role="img" aria-label="Photo of a classroom with pupils raising hands" style="background:linear-gradient(150deg,#d9dfe6,#9aa7b7)"></div>
    <div class="meta"><span>▣ 23rd March 2023</span><span>● Maya Lorne</span></div>
    <h4>Do I Need A TEFL If I Have A PGCE?</h4>
  </article>
  <article class="post" style="left:143px;top:457px">
    <div class="thumb" role="img" aria-label="Photo of hands typing on a laptop at a desk" style="background:linear-gradient(150deg,#c7c2bd,#6c6560)"></div>
    <div class="meta"><span>▣ 23rd March 2023</span><span>● Maya Lorne</span></div>
    <h4>To Be Or Not To Be A Freelance Online English Teacher?</h4>
  </article>
  <article class="post" style="left:455px;top:457px">
    <div class="thumb" role="img" aria-label="Photo of a traveller looking at an airport departure board" style="background:linear-gradient(150deg,#2c3e4c,#5a7282)"></div>
    <div class="meta"><span>▣ 23rd March 2023</span><span>● Maya Lorne</span></div>
    <h4>The Best Countries To Teach English Abroad In 2023</h4>
  </article>
  <article class="post" style="left:763px;top:457px">
    <div class="thumb" role="img" aria-label="Illustration of spring flowers and rabbits for an Easter theme" style="background:linear-gradient(150deg,#efe6d6,#d9b98f)"></div>
    <div class="meta"><span>▣ 23rd March 2023</span><span>● Maya Lorne</span></div>
    <h4>Easter around the World: EFL Classroom Activities</h4>
  </article>
  <a class="btn teal viewall">View All Articles</a>
</section>

<footer class="section footer">
  <svg class="edge" width="1200" height="16" viewBox="0 0 1200 16"><path d="M0 0h1200v6c-40 6-80-4-130 4s-90-6-150 2-100-4-160 3-110-6-170 1-90-4-150 2-120-5-180 2-100-4-150 1-70-3-110 0z" fill="#fff"/></svg>
  <div class="brand"><span class="dot"></span>Linguaro</div>
  <div class="cols">
    <div class="col"><h5>Why Linguaro?</h5><ul><li>Why Choose Us?</li><li>Charity Partnership</li><li>Accreditation</li><li>Compare TEFL Course Providers</li><li>Meet our Alumni</li><li>Meet our Trainers</li><li>Company profile</li><li>Testimonials</li><li>Affiliate Programme</li></ul></div>
    <div class="col"><h5>TEFL Courses</h5><ul><li>View All TEFL Courses</li><li>Online TEFL Course (Level 3 - 120hrs)</li><li>Online TEFL Course (Level 5 - 168hrs)</li><li>Observed Teaching Practice Course (Level 5)</li><li>TEFL Top-Up Courses</li></ul></div>
    <div class="col"><h5>Teaching Opportunities</h5><ul><li>TEFL Jobs</li><li>TEFL Internships</li><li>TEFL Volunteering</li><li>Country Profiles</li><li>Teaching without a Degree</li></ul></div>
    <div class="col"><h5>Student Support Centre</h5><ul><li>TEFL Learning Centre</li><li>Frequently Asked Questions</li></ul></div>
    <div class="col"><h5>Talk to Us</h5><ul><li>Get in Touch</li><li>Request Call Back</li><li>Blog</li></ul></div>
  </div>
  <div class="base">
    <div class="pay"><i></i><i></i><i></i><i></i><i></i><i></i></div>
    <div class="call">Call us for help +1 555 013 4210</div>
    <div class="legal">Linguaro Academy, 18 Harbor Lane, Suite 40, Harbor City, NS 10022, USA.<br>Terms and Conditions &nbsp;|&nbsp; Privacy Policy</div>
    <div class="social"><i></i><i></i><i></i><i></i><i></i></div>
    <div class="copyright">© 2023 Linguaro Academy. All rights reserved.</div>
  </div>
</footer>

</body>
</html>
```